Start-up lawncare company needing marketing flyer to promote business model

Hello! We are looking for a marketing flyer design with the requirements below.

We would like the size to fit a flyer that is 6.25" X 9", Front and Back.

We need these to meet the KBMR ORTQ requirements, there are details attached for the indicias that need to be included, and where to put them on the back of the flyer.

Here's the items items we would like to have included on the flyer:
- Logo (Attached)

- I attached a snip of how our website looks, as well as how our app looks, and would like to follow that general color scheme

- References to our Fernquill App, in both Zenthra and Vorby stores, and our website (www.Fernquill.com)

- Reference to the neighborhood barometer and gets the point across that the more of their neighbors that sign up, the cheaper the price of service (Visual attached of what this barometer looks like)

- We are licensed and insured landscaping pros

- Real, instant, upfront pricing for mowing, mulching and most other services

- Sign up with a few easy steps and manage your account from our app or online

- Automated safe & secure transactions upon service completion and satisfaction

- Excellent customer service with our quality guaranteed commitment!

- Sign up now and receive 50% off your first mow!

- Veteran owned

- A portion of our proceeds go to "Rennick Dolby Foundation"

- List's out all of the services we will offer
- Mowing
- Mulching
- Aeration and Over-seeding
- Fertilization
- Shrub/Tree Trimming
- Leaf removal and yard clean up
- Accent lighting installation
- Sprinkler blow-out / Winterization
- Driveway pressure washing and sealing
- Firewood Delivery

Target Market(s)

Homeowners in large neighborhoods that need lawn care services

Industry/Entity Type

Lawn Care

Font styles to use
Sans Serif

Colors

Designer to choose colors to be used in the design.

Requirements
Must have
• Meet KBMR ORTQ requirements
• Keep a similar color scheme to our website, feel free to use bold accents to make it more eye-catching as people search through their mail
• Get the general point across that as more of their neighbors sign up with us, the cheaper their service will be

```html
<!DOCTYPE html>
<html lang="en">
<head>
<meta charset="utf-8">
<title>Fernquill Flyer – Back</title>
<link href="https://fonts.googleapis.com/css2?family=Poppins:ital,wght@0,500;0,600;0,700;1,600&display=swap" rel="stylesheet">
<style>
  :root{
    --page:#e4e4e4;
    --green-deep:#1b7a36;
    --green-mid:#2f9e44;
    --green-bright:#4cbc3a;
    --lime:#8cc63f;
    --lime-line:#a6d44a;
    --ink-dark:#17602c;
    --white:#ffffff;
    --badge:#2b2b2b;
  }
  *{box-sizing:border-box;margin:0;padding:0}
  html,body{width:1200px;height:1200px;overflow:hidden;background:var(--page);font-family:"Poppins",sans-serif}
  .flyer{position:absolute;left:38px;top:204px;width:1124px;height:790px;overflow:hidden;
    background:linear-gradient(160deg,var(--green-deep) 0%,var(--green-mid) 45%,var(--green-bright) 100%);color:var(--white)}
  .flyer__photo{position:absolute;inset:0;
    background:radial-gradient(ellipse at 72% 58%,rgba(120,210,90,.45),transparent 60%),
               radial-gradient(ellipse at 20% 85%,rgba(20,90,30,.5),transparent 55%);}
  .flyer__wave{position:absolute;inset:0}
  .benefits{position:absolute;left:32px;top:56px;width:574px;height:434px;border:1.5px solid var(--lime-line)}
  .benefit{position:absolute;left:17px;display:flex;align-items:center}
  .benefit__icon{width:74px;height:74px;border-radius:50%;border:2px solid var(--lime-line);background:var(--green-mid);
    display:flex;align-items:center;justify-content:center;flex-shrink:0}
  .benefit__text{margin-left:15px;font-size:19.5px;font-weight:600;line-height:24px;letter-spacing:.9px;white-space:nowrap}
  .services-tab{position:absolute;left:584px;top:36px;width:328px;height:96px;background:var(--lime);
    clip-path:polygon(0 0,100% 0,88% 100%,0 100%);display:flex;align-items:center;padding-left:39px}
  .services-tab h2{font-size:28px;font-weight:700;color:var(--ink-dark);letter-spacing:.8px}
  .services{position:absolute;left:626px;top:114px;width:432px;height:376px;border:1.5px solid var(--lime-line);border-top-color:transparent}
  .services ul{list-style:none;position:absolute;left:18px;top:54px}
  .services li{font-size:18.5px;font-weight:600;line-height:28.7px;letter-spacing:.2px;white-space:nowrap}
  .services li::before{content:"•"}
  .mail-box{position:absolute;background:var(--white);border:1.5px solid #222}
  .mail-box--permit{left:979px;top:477px;width:89px;height:89px}
  .mail-box--address{left:732px;top:614px;width:304px;height:120px}
  .brand-tile{position:absolute;left:33px;top:586px;width:155px;height:156px;background:var(--white);border-radius:16px;
    display:flex;align-items:center;justify-content:center}
  .brand-tile__name{font-size:25px;font-weight:700;color:var(--green-deep)}
  .cta{position:absolute;left:210px;top:583px}
  .cta__title{font-size:28px;font-weight:600;line-height:35px;letter-spacing:1.2px}
  .stores{display:flex;gap:19px;margin-top:12px;margin-left:6px}
  .store{width:136px;height:45px;background:var(--badge);border-radius:5px;border:1px solid #555;
    padding:4px 10px;display:flex;flex-direction:column;justify-content:center}
  .store__small{font-size:7.5px;font-weight:500;line-height:9px;white-space:nowrap}
  .store__big{font-size:17px;font-weight:500;line-height:20px;white-space:nowrap}
  .cta__web{margin-top:14px;font-size:24px;font-weight:600;letter-spacing:.9px;white-space:nowrap}
  .cta__web em{font-style:italic}
</style>
</head>
<body>
<main class="flyer">
  <div class="flyer__photo" role="img" aria-label="Photo of a lawn mower cutting grass, tinted green"></div>
  <svg class="flyer__wave" width="1124" height="790" viewBox="0 0 1124 790" aria-hidden="true">
    <path d="M0 0 H1124 V120 C970 150 850 140 750 120 C590 80 410 -10 200 10 C120 18 50 40 0 60 Z" fill="#1a7433" opacity=".55"/>
    <path d="M0 60 C200 10 410 40 590 110 C690 150 810 170 950 150 L950 170 C790 200 630 180 510 140 C350 90 180 80 0 120 Z" fill="#39a845" opacity=".35"/>
  </svg>

  <section class="benefits">
    <div class="benefit" style="top:19px">
      <div class="benefit__icon"><svg width="40" height="40" viewBox="0 0 40 40"><circle cx="20" cy="20" r="14" fill="none" stroke="#fff" stroke-width="2.5"/><text x="20" y="27" font-size="20" font-weight="700" fill="#fff" text-anchor="middle" font-family="Poppins,sans-serif">$</text></svg></div>
      <p class="benefit__text">Real, instant, upfront pricing for mowing,<br>mulching and most other services</p>
    </div>
    <div class="benefit" style="top:101px">
      <div class="benefit__icon"><svg width="40" height="40" viewBox="0 0 40 40" fill="none" stroke="#fff" stroke-width="2.5"><rect x="5" y="7" width="30" height="20" rx="2"/><path d="M20 27v6M13 34h14"/></svg></div>
      <p class="benefit__text">Automated safe &amp; secure transactions<br>upon service completion and satisfaction</p>
    </div>
    <div class="benefit" style="top:181px">
      <div class="benefit__icon"><svg width="40" height="40" viewBox="0 0 40 40" fill="none" stroke="#fff" stroke-width="2.5"><circle cx="20" cy="20" r="14"/><path d="M13 20l5 5 9-10"/></svg></div>
      <p class="benefit__text">Excellent customer service with our<br>quality guaranteed commitment!</p>
    </div>
    <div class="benefit" style="top:262px">
      <div class="benefit__icon"><svg width="40" height="40" viewBox="0 0 40 40" fill="#fff"><circle cx="20" cy="16" r="6"/><path d="M9 33c0-7 5-10 11-10s11 3 11 10z"/></svg></div>
      <p class="benefit__text">Veteran owned</p>
    </div>
    <div class="benefit" style="top:343px">
      <div class="benefit__icon"><svg width="40" height="40" viewBox="0 0 40 40" fill="none" stroke="#fff" stroke-width="2.5"><path d="M6 22l8-8 6 4 6-4 8 8-10 8-4-3-4 3z"/></svg></div>
      <p class="benefit__text">A portion of our proceeds go to<br>"Rennick Dolby Foundation"</p>
    </div>
  </section>

  <div class="services-tab"><h2>OUR SERVICES</h2></div>
  <section class="services">
    <ul>
      <li>Mowing</li>
      <li>Mulching</li>
      <li>Aeration and Over-seeding</li>
      <li>Fertilization</li>
      <li>Shrub/Tree Trimming</li>
      <li>Leaf removal and yard clean up</li>
      <li>Accent lighting installation</li>
      <li>Sprinkler blow-out / Winterization</li>
      <li>Driveway pressure washing and sealing</li>
      <li>Firewood Delivery</li>
    </ul>
  </section>

  <div class="mail-box mail-box--permit" aria-label="Postage indicia area"></div>
  <div class="mail-box mail-box--address" aria-label="Mailing address area"></div>

  <div class="brand-tile"><span class="brand-tile__name">Fernquill</span></div>

  <section class="cta">
    <h3 class="cta__title">DOWNLOAD OUR APP &amp;<br>SIGN UP NOW</h3>
    <div class="stores">
      <div class="store"><span class="store__small">Available on the Vorbyphone</span><span class="store__big">Vorby Store</span></div>
      <div class="store"><span class="store__small">ZENTHROID APP ON</span><span class="store__big">Zenthra play</span></div>
    </div>
    <p class="cta__web"><em>Visit Us at</em> WWW.FERNQUILL.COM</p>
  </section>
</main>
</body>
</html>
```